■依頼の目的/概要
ベストセラー作家が送る最新作の表紙を飾りませんか?
Borelo QuillのBWSの電子書籍表紙デザインをお願いします。

■本の内容
*タイトル:
うつむく朝に灯すひと匙の言葉

というタイトルの表紙デザインの発注になります。

■デザイン要望

要望1つ目
作家名は後でお伝えします。作家名もどこかに挿入いただきたいです。よろしくお願いします。
提出の際は ○○著という形でご提出よろしくお願いします。

要望2つ目
ウェルネスバランスコーチ検定資格保持者

とどこかに入れてください。

要望3つ目
累計Borelo 1位〇冠
(現在、59冠までいっています。今後、出版が控えている作品があります。
そのため、その最終冠数を入れて頂きたいです。)

とどこかに入れてください。

また、出来上がったデザインを作家グループの中で投票にかけて、
一番投票得票数の多かったものを表紙デザインとして選ばせていただきたいと考えております。
もしかしたら、その中で、何か修正依頼など来るかもしれませんが、
それも含めて、ご対応していただける方よろしくお願いします。

また、最終、選考後、
累計Borelo 1位〇〇冠   と記載された表紙と、
累計Borelo 1位〇〇冠   と記載されない表紙の
2表紙の納品をよろしくお願いします。他の部分の表紙のデザイン変更は不要です。
(これは、最終選ばれたデザイナーさんのみご対応で大丈夫です。)

お手数をおかけしますが、よろしくお願いします。

1部内容の抜粋を記載します。

データサイズですが、推奨サイズでJPEGファイルでご納品下さい、よろしくお願いします。
(推奨サイズは2560×1600pxです。)
その他何かご不明な点がございましたら、お気軽にご質問下さい。
よろしくお願いいたします。
変更点がでてきました。

累計Borelo 1位〇〇冠→累計Borelo 1位65冠
と決定しました。最終、この数字でご納品ください。

もうすでに提出済みの方に関しましては、当選後のご対応で大丈夫です。
お手数をおかけしますが、ご対応なにとぞよろしくお願いいたします。
皆様、たくさんのご応募まことにありがとうございました。
コンペというとても厳しい条件にも関わらず、挑戦いただいたことに
大変大変感謝しております。
ご提案されましたすべての作品、デザイナー様のご経歴、作成への思い入れ、
すべてを拝見させていただきました。
これから、作家グループへ全体回覧のメールを致します。
作家グループの皆様の投票結果までお待ちください(場合により結果
公表まで1週間から10日ぐらいかかる場合もあると思われます)。
また、この度、いろいろな作品に触れさせていただきましたこと本当に
本当に感謝いたします。
皆さまのご努力、精進そしてそのチャレンジに大変感謝と尊敬を感じております。
ご経歴やデザイナー様の名前などすべて伏せて、作品のみの提示にて
小説家作家グループに提案させていただきたいと思っております。
ただ、今回の表紙に関しましては、どうしても1名しか選べない状況がございますこと
また、総選挙による投票にて決定致しますこと、ご理解何卒よろしくお願い申しあげます。
また、もしも、今回当選に至らないことがありましても、
今後も私自身は作家生活を継続予定ですので、
(今回は作品の表紙に合わないことがあっても)作風の気に入ったデザイナー様には
個人的にお話を相談させていただく場合もあると思っております。
また、別の作品の表紙を飾っていただく可能性もあるかと思っております。
この度は誠に誠にありがとうございました。
表紙ですが、最終選考決定いたしました。
当選された方には個別に連絡をさせていただきました。

皆様からのご提案、そして、そのチャレンジに敬意と感謝をしております。
私はこれからも作家活動を継続致しますので、また、ご一緒にお仕事をさせていただき
表紙を飾っていただく機会もあるかと思います。
その際はなにとぞよろしくお願いもうしあげます。
自分のためだけでなく、ベストセラーを取り続けることで、素晴らしい表紙を飾れるチャンスをこれからも作りたいと思い、また、精進していきたいと思います。
この度はまことにありがとうございました。

「目が惹きつけられました」とか
これから上を向いて、光を見て行こうとする視線と深く、それでいて爽やかなブルーのタッチがとても印象的で綺麗‼️
など目が離せない、というようなコメントを多くいただきました。
ご提出誠にありがとうございます。

コンペについてはとても厳しい条件にも関わらず挑戦していただき、
本当に一つのタイトルに対する皆様の創造力について驚きや才能についてをいつも
感じています。
そして、そのチャレンジする姿勢にいつもエネルギーをいただき、
私自身もこれからも、いろいろなことに挑戦する姿勢を続けていきたいな、
と感じております。
表紙を飾っていただく機会もあるかと思います。
その際はなにとぞよろしくお願いもうしあげます。この度はありがとうございました。

```html
<!DOCTYPE html>
<html lang="ja">
<head>
<meta charset="utf-8">
<title>うつむく朝に灯すひと匙の言葉</title>
<link rel="stylesheet" href="https://fonts.googleapis.com/css2?family=Noto+Sans+JP:wght@400;500;700;900&family=Noto+Serif+JP:wght@500;700;900&display=swap">
<style>
  :root {
    --sky: #d3e9f8;
    --frame: #ffffff;
    --ink: #111111;
    --heart-top: #f6a5b2;
    --heart-bottom: #e0607a;
    --badge: #d9ecfa;
    --badge-ring: #ffffff;
    --ribbon: #e2c77d;
    --ribbon-dark: #c8a85a;
    --rule: #222222;
  }
  * { margin: 0; padding: 0; box-sizing: border-box; }
  html, body { width: 758px; height: 1200px; overflow: hidden; background: #ffffff; }
  .cover {
    position: relative;
    width: 758px; height: 1200px;
    background: var(--sky);
    border: 14px solid var(--frame);
    font-family: "Noto Sans JP", sans-serif;
    color: var(--ink);
    overflow: hidden;
  }
  .title-lead {
    position: absolute; top: 38px; left: 0; right: 0;
    text-align: center; font-weight: 900; font-size: 60px; letter-spacing: 2px;
  }
  .heart {
    position: absolute; top: 130px; left: 115px; width: 500px; height: 230px;
  }
  .title-key {
    position: absolute; top: 165px; left: 0; right: 0;
    text-align: center; font-weight: 900; font-size: 140px; line-height: 1;
  }
  .title-particle {
    position: absolute; top: 350px; left: 0; right: 0;
    text-align: center; font-weight: 900; font-size: 110px; line-height: 1;
  }
  .title-main {
    position: absolute; top: 465px; left: 0; right: 0;
    text-align: center; font-weight: 900; font-size: 170px; line-height: 1; letter-spacing: 6px;
  }
  .tagline {
    position: absolute; top: 650px; left: 40px; right: 40px;
    text-align: center; font-weight: 500; font-size: 23px;
    padding-bottom: 8px; border-bottom: 2px solid var(--rule);
  }
  .topic {
    position: absolute; top: 695px; left: 40px;
    font-weight: 900; font-size: 44px; line-height: 1.2;
  }
  .contents {
    position: absolute; top: 808px; left: 40px; width: 430px;
    list-style: none; font-size: 17px; font-weight: 500; line-height: 1.45;
  }
  .contents li { padding-left: 20px; position: relative; }
  .contents li::before {
    content: ""; position: absolute; left: 0; top: 6px;
    width: 12px; height: 12px; border: 1.5px solid var(--ink); background: #fff;
  }
  .badge { position: absolute; top: 770px; left: 470px; width: 240px; height: 230px; }
  .badge-text {
    position: absolute; top: 790px; left: 470px; width: 240px;
    text-align: center; font-family: "Noto Serif JP", serif; font-weight: 900; line-height: 1.05;
  }
  .badge-text .small { font-size: 22px; display: block; }
  .badge-text .rank { font-size: 58px; display: block; margin-top: 4px; }
  .badge-text .count { font-size: 50px; display: block; }
  .ribbon-label {
    position: absolute; top: 963px; left: 470px; width: 240px;
    text-align: center; font-family: "Noto Serif JP", serif; font-weight: 700; font-size: 19px; color: #fff;
  }
  .closing {
    position: absolute; top: 1030px; left: 40px;
    font-weight: 900; font-size: 48px; letter-spacing: 1px;
  }
  .credit {
    position: absolute; top: 1125px; left: 40px; right: 40px;
    display: flex; justify-content: space-between; align-items: baseline;
    font-size: 16px; font-weight: 500;
  }
  .credit .author { font-size: 30px; font-weight: 700; letter-spacing: 2px; }
</style>
</head>
<body>
<main class="cover">
  <h1>
    <span class="title-lead">うつむく朝に灯す</span>
    <svg class="heart" viewBox="0 0 500 230" role="img" aria-label="ハート型のピンクのグラデーション装飾">
      <defs>
        <linearGradient id="heartFill" x1="0" y1="0" x2="0" y2="1">
          <stop offset="0" stop-color="var(--heart-top)"/>
          <stop offset="1" stop-color="var(--heart-bottom)"/>
        </linearGradient>
      </defs>
      <path d="M250 225 C 110 160 10 110 10 60 C 10 20 60 2 120 2 C 180 2 230 25 250 55 C 270 25 320 2 380 2 C 440 2 490 20 490 60 C 490 110 390 160 250 225 Z" fill="url(#heartFill)"/>
    </svg>
    <span class="title-key">ひと匙</span>
    <span class="title-particle">の</span>
    <span class="title-main">言葉</span>
  </h1>

  <p class="tagline">ウェルネスバランスコーチ検定資格保持者が語る</p>

  <h2 class="topic">ウェルネス<br>バランス</h2>

  <ul class="contents">
    <li>その原因を探ってみよう</li>
    <li>落ち込んだ理由について</li>
    <li>人間関係がその悩みの根本だと気づいたとき</li>
    <li>お金に困ったとき</li>
    <li>繰り返しつらいことを考えてしまうとき</li>
    <li>落ち込んだ時の対処法</li>
    <li>今、自分ができること、やってみたいことを<br>書き出してみよう</li>
  </ul>

  <svg class="badge" viewBox="0 0 240 230" aria-hidden="true">
    <circle cx="120" cy="105" r="100" fill="var(--badge)" stroke="var(--badge-ring)" stroke-width="5"/>
    <path d="M10 175 L230 175 L220 195 L230 215 L10 215 L20 195 Z" fill="var(--ribbon-dark)"/>
    <rect x="22" y="172" width="196" height="40" fill="var(--ribbon)"/>
  </svg>
  <div class="badge-text">
    <span class="small">累計</span>
    <span class="small">BORELO</span>
    <span class="rank">1位</span>
    <span class="count">59冠</span>
  </div>
  <div class="ribbon-label">ベストセラー作家</div>

  <p class="closing">自分らしく生きるために</p>

  <p class="credit">
    <span>ウェルネスバランスコーチ検定資格保持者</span>
    <span class="author">○○○○著</span>
  </p>
</main>
</body>
</html>
```